Unique E-commerce website needs a FLAT UI design

Looking for creative website designer / company to design a flat ui interface for the main 4 pages.

I SEEK FLAT UI DESIGN ONLY - this means nice, clean and modern design,

As we're dealing with the design of the main pages this will define the overall site design so take a moment or two to think on the audience and create an appealing branding.

Website design must be mobile/ipad friendly.

I've written a detailed design requirements document for those 4 pages.
Please read it carefully and make sure you understand every aspect of it before starting the design process.
You can find a brief intro text and some reference designs that I like to get you started.

This is not a closed concept, I'm open to hear new ideas and ways to improve the UI/UX.

Feel free to ask anything, I'm available most of the day.

I'm looking to build a long term relationship as this is the first phase of the design, I have 1-2 phases to come.

Target Market(s)

Online shoppers age between 18-60 that buy frequently at US merchants

Industry/Entity Type

It Company

Number of Pages Required

4 page

Requirements
Must have
• Flat UI design
• Flat colors
• Modern, clean and easy to follow design
Nice to have
• Original icons for the features page

```html
<!DOCTYPE html>
<html lang="en">
<head>
<meta charset="utf-8">
<title>ParcelPort – FAQ</title>
<link href="https://fonts.googleapis.com/css2?family=Montserrat:wght@400;600;700&family=Open+Sans:wght@400;600&display=swap" rel="stylesheet">
<style>
:root{
  --header-bg:#67b0d4;
  --header-line:#559fc4;
  --accent:#f4c747;
  --white:#ffffff;
  --ink:#222222;
  --body:#666666;
  --rule:#e3e3e3;
  --side-head:#f2f2f2;
  --footer-bg:#253447;
  --footer-base:#1f2b3a;
  --footer-head:#8794a4;
  --footer-link:#a9b4c1;
  --footer-icon:#3b4b5f;
}
*{margin:0;padding:0;box-sizing:border-box}
html,body{width:1041px;height:1200px;overflow:hidden;background:var(--white)}
body{position:relative;font-family:'Open Sans',Arial,sans-serif}
.site-header{position:absolute;top:0;left:0;width:1041px;height:75px;background:var(--header-bg);border-bottom:1px solid var(--header-line)}
.brand{position:absolute;left:92px;top:28px;font-family:'Montserrat',Arial,sans-serif;font-weight:700;font-size:19px;letter-spacing:.3px;color:var(--white)}
.main-nav{position:absolute;left:288px;top:0;height:75px;display:flex}
.nav-item{height:75px;border-left:1px solid var(--header-line);display:flex;flex-direction:column;align-items:center;justify-content:flex-end;padding-bottom:16px;font-family:'Montserrat',Arial,sans-serif;font-weight:700;font-size:10.5px;color:var(--white);text-transform:uppercase}
.nav-item:last-child{border-right:1px solid var(--header-line)}
.nav-item svg{margin-bottom:8px}
.nav-item.is-user{color:var(--accent)}
.caret{display:inline-block;margin-left:5px;border:4px solid transparent;border-top:4px solid currentColor;border-bottom:0;vertical-align:middle}
.faq-nav{position:absolute;left:90px;top:100px;width:198px;border-top:1px solid var(--rule)}
.faq-nav li{list-style:none;height:39.5px;border-bottom:1px solid var(--rule);border-left:1px solid var(--rule);padding-left:11px;padding-right:16px;display:flex;align-items:center;justify-content:space-between;white-space:nowrap;font-family:'Montserrat',Arial,sans-serif;font-size:12px;letter-spacing:-.1px;color:var(--ink)}
.faq-nav li.faq-title{background:var(--side-head);font-size:13.5px;height:38px}
.down{border:6px solid transparent;border-top:7px solid #bbb;border-bottom:0}
.side-rule{position:absolute;left:288px;top:75px;width:1px;height:895px;background:var(--rule);box-shadow:2px 0 4px rgba(0,0,0,.05)}
.faq-section{position:absolute;left:313px;width:638px;font-size:11.8px;letter-spacing:-.08px;line-height:17.6px;color:var(--body);hyphens:auto;-webkit-hyphens:auto}
.faq-section h2{font-family:'Montserrat',Arial,sans-serif;font-size:15px;font-weight:600;color:var(--ink);margin-bottom:9px;line-height:20px;letter-spacing:0}
.faq-section p{margin-bottom:17.6px}
.steps{padding-left:11px;margin-bottom:17.6px}
.site-footer{position:absolute;left:0;top:970px;width:1041px;height:170px;background:var(--footer-bg)}
.footer-col{position:absolute;top:27px}
.footer-col h3{font-family:'Open Sans',Arial,sans-serif;font-size:11px;font-weight:600;letter-spacing:.3px;color:var(--footer-head);text-transform:uppercase;margin-bottom:14px}
.footer-col a{display:block;font-size:12px;line-height:17.6px;color:var(--footer-link);text-decoration:none}
.social h3{margin-bottom:9px}
.social a{display:flex;align-items:center;height:22px;margin-bottom:6px}
.social span{width:22px;height:22px;background:var(--footer-icon);margin-right:8px;display:inline-block}
.pay-name{font-family:'Open Sans',Arial,sans-serif;font-size:16px;font-weight:600;color:var(--footer-link);margin-top:-4px;margin-bottom:14px}
.partner-badge{width:130px;height:23px;background:var(--footer-icon);margin-top:-6px}
.footer-base{position:absolute;left:0;top:1140px;width:1041px;height:60px;background:var(--footer-base);text-align:center;line-height:52px;font-size:11px;color:var(--footer-link)}
</style>
</head>
<body>
<header class="site-header">
  <div class="brand">PARCELPORT</div>
  <nav class="main-nav">
    <div class="nav-item" style="width:79px"><svg width="24" height="16"><rect width="24" height="16" fill="#fff"/><rect y="3" width="24" height="2" fill="#e04b4b"/><rect y="8" width="24" height="2" fill="#e04b4b"/><rect y="13" width="24" height="2" fill="#e04b4b"/><rect width="10" height="8" fill="#3d5fa8"/></svg><span>USA<i class="caret"></i></span></div>
    <div class="nav-item" style="width:94px"><svg width="26" height="26"><circle cx="13" cy="13" r="11" fill="#7b8a96"/><circle cx="13" cy="13" r="4" fill="#c7d0d6"/></svg><span>Features</span></div>
    <div class="nav-item" style="width:85px"><svg width="24" height="24"><rect width="24" height="24" rx="2" fill="#5e8f3e"/><circle cx="12" cy="12" r="5" fill="#9cc46a"/></svg><span>Pricing</span></div>
    <div class="nav-item" style="width:65px"><svg width="24" height="24"><circle cx="12" cy="12" r="10" fill="none" stroke="#fff" stroke-width="5"/><circle cx="12" cy="12" r="10" fill="none" stroke="#e24a3b" stroke-width="5" stroke-dasharray="8 7.7"/></svg><span>Help</span></div>
    <div class="nav-item" style="width:167px"><svg width="24" height="24"><rect width="24" height="24" rx="2" fill="#f0c36a"/><rect x="2" y="2" width="9" height="9" fill="#fff"/><rect x="13" y="2" width="9" height="9" fill="#fff"/><rect x="2" y="13" width="9" height="9" fill="#fff"/><rect x="13" y="13" width="9" height="9" fill="#fff"/></svg><span>Shipping Calculators<i class="caret"></i></span></div>
    <div class="nav-item" style="width:74px"><svg width="24" height="24"><path d="M6 22l2-7L17 4l4 4-11 9z" fill="#f29b3c"/></svg><span>Sign In</span></div>
    <div class="nav-item is-user" style="width:97px"><svg width="24" height="24" role="img" aria-label="User avatar"><circle cx="12" cy="12" r="11" fill="#f0a45a"/></svg><span>Nickname<i class="caret"></i></span></div>
  </nav>
</header>

<ul class="faq-nav">
  <li class="faq-title">FAQ</li>
  <li>Introduction</li>
  <li>Control Panel</li>
  <li>Shipping <i class="down"></i></li>
  <li>Package handling &amp; Services</li>
  <li>Pricing &amp; Billing</li>
  <li>Shipping</li>
</ul>
<div class="side-rule"></div>

<section class="faq-section" style="top:109px">
  <h2>Who is ParcelPort for?</h2>
  <p>ParcelPort is a platform that enables shoppers all around the globe purchasing from any online US store. We have set ourselves a goal to break geographical boundaries and to enable non US shoppers to purchase freely from any merchant in the US and get the goods delivered seamlessly. Every registered member receives a private US shipping address that can be used as the shipping address for all US purchases.</p>
  <p>We offer significantly low shipping rates bundled with advanced shipment tracking system, comprehensive shipping insurance policy and full range of extra services that can save you both time and money.</p>
  <p>In many cases it would be cheaper to use our services to deliver order abroad than having it delivered directly through the merchant. Check out our shipping costs calculators to see it for yourself.</p>
</section>

<section class="faq-section" style="top:337px">
  <h2>How it works</h2>
  <p>You're only a step away from the hottest brands and the wildest sales you have ever dreamed of. A world of thousands US merchants is just a click away. Tired of the days where a pop up message saying that shipping is only limited to the US has stood between you and a crazy sale? Guess what? those days are over, follow the steps bellow and start your amazing shopping spree today!</p>
  <div class="steps">
    <div>- Open a new account, it only takes 10 seconds to complete and receive your private shipping address.</div>
    <div>- Shop in any US online store and use your private shipping address to deliver your orders to our distribution center.</div>
    <div>- We will notify you the moment your order arrives at your private address.</div>
    <div>- Log in into your control panel to see your incoming packages, order extra services and have your orders prepared for shipping.</div>
  </div>
  <p>Don't forget to check out our detailed FAQ section to get you started right away. We highly recommend you to dedicate some time to read our comprehensive tutorials zone to learn how to perform common tasks. Additionally, you can always contact our customer support to receive dedicated support.</p>
</section>

<section class="faq-section" style="top:651px;left:311px">
  <h2>What we do better?</h2>
  <p>We believe in honesty and playing fair therefore, customers are only charged for services they use. No subscriptions or hidden fees, our pricing charts include all charges and everything is transparent. We also believe in technology to make a fantastic user experience, to answer that need we've designed state of the art control panel to manage both incoming packages and orders, and to purchase extra services all in one place. Additionally, every shipment includes a tracking number so you can always keep an eye on your goods and for maximum protection you can also purchase a shipping insurance - we offer the lowest rates in the industry.</p>
  <p>Wait no more and start your US shopping spree with us today!</p>
</section>

<section class="faq-section" style="top:863px;left:311px">
  <h2>Why our rates are significantly low?</h2>
  <p>We put our customers upfront and always try come up with lower pricing. You can rest assured that your goods are handled professionally by our trained operations staff and that you get the best services out there.</p>
</section>

<footer class="site-footer">
  <div class="footer-col" style="left:91px"><h3>Overview</h3><a>Features</a><a>Pricing</a><a>Package Calculator</a><a>Bazaar Calculator</a></div>
  <div class="footer-col" style="left:273px"><h3>Company</h3><a>About Us</a><a>Contact</a></div>
  <div class="footer-col" style="left:436px"><h3>Help</h3><a>Shipping</a><a>Pricing &amp; Billing</a><a>Services</a><a>Tutorials</a></div>
  <div class="footer-col social" style="left:621px"><h3>Connect</h3><a><span></span>TubeCast</a><a><span></span>Circlebook</a><a><span></span>Chirper</a></div>
  <div class="footer-col" style="left:803px"><h3>Accepting</h3><div class="pay-name">CoinRail</div><h3>In Partnership</h3><div class="partner-badge"></div></div>
</footer>
<div class="footer-base">Copyright © 2014. Northfield . Terms · Privacy</div>
</body>
</html>
```